Brindle Institute Sydney Counsellor iPhone app design

Live wireframes are here;

https://view.frameloft-demo.com/8a2c41d7e09b3f56c1a47d280e9b5c3f61d2a07b#/pages/42918806

Password - brindlesyd482!

We're nearing completion of the Blueprinting phase for our app development project for Brindle Institute Sydney. We need a designs matching the attached functional specification we've created for the app.

VISION
The Sydney Brindle Institute Counselling Services app provides simple and accessible information and engagement with mobile relevant services.
Opening the app, users are greeted with a simple “Hello, how are you today?” a 3 multiple choice answers to both aid in contextual content presentation/navigation specific to the users needs.
Users can access a range of existing web resources from the current website via live in app content and web links. Users can also access a personal folder storing PDF’s that are shared as part of meetings with Brindle Institute Counsellors.
The app also features evolving content pulling from the existing WIKI and presents new and user relevant updates upon opening the app.
Finally, the solution will also deliver support to senior counsellors on each campus by streamlining tasks (such as booking appointments etc). The solution will also provide counsellors with notifications on students at risk and who may need greater support on their journeys.

Target Market(s)

People aged 15 to 24 years
• Students in this age group represent the largest market for
the industry, accounting for an estimated 44.7% of industry revenue in 2014-15. Demand for vocational education from school leavers has declined, as government reforms in higher education have led to more available university places for undergraduate students. Consequently, this market has declined in its share of revenue over the past five years.

People aged 25 to 44 years
• People aged 25 to 44 years are estimated to account for
37.2% of industry revenue. This market has grown its share of revenue over the past five years, as many Australians are entering the system to retrain or update workforce skills due to structural changes occurring in the economy. Students in this age group typically work full- time and therefore undertake their studies part-time, either on-campus or through distance learning.

People aged 45 years and over
• Individuals in this market represent 18.1% of the industry.
The majority of students in this age group have well- established careers, so students undertaking vocational courses are either seeking to upskill or have decided to change careers. As many of these students are employed full-time and often have family commitments, they require more flexible class schedules. This market has remained relatively stable as a share of revenue over the past five years.

Industry/Entity Type

Counsellor

Font styles to use
Sans Serif

Requirements
Must have
• The app needs to meet accessibility guidelines, so no text in images, nice flat design etc.
• The wireframes attached are not to spec, they're just a guide.
• Designs must meet the Apple interface guidelines and device specs for iPhone 4s, 5, 5s, 6 6+
• We also need an app store logo.
Nice to have
• NA

```html
<!DOCTYPE html>
<html lang="en">
<head>
<meta charset="utf-8">
<title>Brindle Institute Counselling – App Screens</title>
<link rel="stylesheet" href="https://fonts.googleapis.com/css2?family=Raleway:wght@400;500;600;700&display=swap">
<style>
  :root {
    --stage: #5e5f6e;
    --brand: #e8425f;
    --ink: #3a3a3a;
    --muted: #777777;
    --rule: #dddddd;
    --paper: #ffffff;
    --scrim: rgba(110, 110, 110, 0.78);
    --star: #f4c11d;
    --star-outline: #9a9a9a;
  }
  * { box-sizing: border-box; margin: 0; padding: 0; }
  html, body { width: 1200px; height: 790px; overflow: hidden; }
  body {
    background: var(--stage);
    font-family: "Raleway", Arial, sans-serif;
    color: var(--ink);
    position: relative;
  }
  .screen-row {
    position: absolute;
    left: 60px; top: 111px;
    display: flex; gap: 60px;
  }
  .screen {
    width: 320px; height: 568px;
    background: var(--paper);
    position: relative;
    overflow: hidden;
    box-shadow: 0 12px 30px rgba(0,0,0,0.25);
  }
  .status-bar {
    height: 20px; background: var(--brand);
    color: #fff; font-size: 10px; font-weight: 600;
    display: flex; align-items: center; justify-content: space-between;
    padding: 0 6px; position: relative;
  }
  .status-bar .time { position: absolute; left: 0; right: 0; text-align: center; pointer-events: none; }
  .nav-bar {
    height: 44px; background: var(--brand);
    display: flex; align-items: center; justify-content: center;
    position: relative; color: #fff; font-size: 16px; font-weight: 600;
  }
  .nav-bar .menu-toggle { position: absolute; left: 12px; top: 15px; }

  /* Articles & contacts lists */
  .list-item {
    padding: 16px 16px 14px;
    border-bottom: 1px solid var(--rule);
  }
  .article { display: flex; gap: 10px; }
  .article .star { flex: none; margin-top: 1px; }
  .item-title { font-size: 15px; font-weight: 700; margin-bottom: 6px; }
  .item-body { font-size: 11px; line-height: 1.45; color: var(--muted); }
  .read-more { display: inline-block; margin-top: 5px; font-size: 11px; font-weight: 600; color: var(--brand); }

  .contact-head { display: flex; justify-content: space-between; align-items: center; margin-bottom: 6px; }
  .contact-head .item-title { margin: 0; text-decoration: underline; }
  .contact-tools { display: flex; gap: 10px; }
  .phone-line { margin-top: 5px; font-size: 11px; color: var(--muted); }
  .phone-line b { color: var(--brand); font-weight: 600; }

  /* Menu drawer */
  .home-prompt {
    position: absolute; right: 6px; bottom: 70px;
    font-size: 14px; font-weight: 600; white-space: nowrap;
  }
  .scrim { position: absolute; left: 0; right: 0; top: 64px; bottom: 0; background: var(--scrim); }
  .drawer {
    position: absolute; left: 0; top: 64px; bottom: 0; width: 240px;
    background: var(--paper);
  }
  .drawer-welcome {
    padding: 18px 14px 12px; text-align: center;
    font-size: 14px; font-weight: 500; line-height: 1.4;
  }
  .drawer-account {
    display: flex; flex-direction: column; align-items: center; gap: 6px;
    padding: 6px 0 16px; font-size: 11px; color: var(--muted);
    border-bottom: 1px solid var(--rule);
  }
  .drawer-nav { list-style: none; }
  .drawer-nav li {
    display: flex; align-items: center; gap: 12px;
    height: 40px; padding: 0 16px; font-size: 13px;
    border-bottom: 1px solid var(--rule);
  }
  .drawer-nav li.is-active { background: var(--brand); color: #fff; }
</style>
</head>
<body>
<main class="screen-row">

  <!-- Menu screen -->
  <section class="screen menu-screen">
    <div class="status-bar"><span>Carrier</span><span class="time">5:21 PM</span><span>100%</span></div>
    <header class="nav-bar">
      <svg class="menu-toggle" width="18" height="14" viewBox="0 0 18 14"><path d="M0 1h18M0 7h18M0 13h18" stroke="#fff" stroke-width="2"/></svg>
      Menu
    </header>
    <p class="home-prompt">Articles?</p>
    <div class="scrim"></div>
    <nav class="drawer">
      <p class="drawer-welcome">Welcome to Brindle Institute Counselling?<br>How can we help you?</p>
      <div class="drawer-account">
        <svg width="22" height="16" viewBox="0 0 22 16"><rect x="1" y="1" width="20" height="14" fill="none" stroke="#888" stroke-width="1.4"/><path d="M1 1l10 8 10-8" fill="none" stroke="#888" stroke-width="1.4"/></svg>
        <span>student.help@brindle-inst.edu.au</span>
      </div>
      <ul class="drawer-nav">
        <li class="is-active"><svg width="16" height="14" viewBox="0 0 16 14"><path d="M1 7L8 1l7 6M3 6v7h10V6" fill="none" stroke="#fff" stroke-width="1.4"/></svg>Home</li>
        <li><svg width="16" height="14" viewBox="0 0 16 14"><rect x="1" y="1" width="14" height="12" fill="none" stroke="#666" stroke-width="1.3"/><path d="M4 5h8M4 8h8M4 11h5" stroke="#666"/></svg>Articles</li>
        <li><svg width="16" height="14" viewBox="0 0 16 14"><path d="M3 1l3 3-2 2c1 2 2 3 4 4l2-2 3 3-2 2C6 13 2 9 1 3z" fill="#666"/></svg>Contacts</li>
        <li><svg width="16" height="14" viewBox="0 0 16 14"><circle cx="8" cy="4" r="3" fill="#666"/><path d="M2 14c0-4 3-6 6-6s6 2 6 6z" fill="#666"/></svg>Profile</li>
        <li><svg width="16" height="14" viewBox="0 0 16 14"><circle cx="8" cy="7" r="6" fill="none" stroke="#666" stroke-width="1.3"/><path d="M8 6v4M8 4v.5" stroke="#666" stroke-width="1.5"/></svg>About</li>
      </ul>
    </nav>
  </section>

  <!-- Contacts screen -->
  <section class="screen contacts-screen">
    <div class="status-bar"><span>Carrier</span><span class="time">5:21 PM</span><span>100%</span></div>
    <header class="nav-bar">
      <svg class="menu-toggle" width="18" height="14" viewBox="0 0 18 14"><path d="M0 1h18M0 7h18M0 13h18" stroke="#fff" stroke-width="2"/></svg>
      Contacts
    </header>
    <article class="list-item">
      <div class="contact-head"><h2 class="item-title">Ashgrove</h2>
        <span class="contact-tools">
          <svg width="12" height="14" viewBox="0 0 12 14"><path d="M1 3h10M4 3V1h4v2M2 3l1 10h6l1-10" fill="none" stroke="#555" stroke-width="1.3"/></svg>
          <svg width="12" height="14" viewBox="0 0 12 14"><path d="M6 13C2 8 1 6 1 5a5 5 0 0110 0c0 1-1 3-5 8z" fill="none" stroke="#555" stroke-width="1.3"/><circle cx="6" cy="5" r="1.6" fill="#555"/></svg>
        </span></div>
      <p class="item-body">Lorem Ipsum is simply dummy text of the printing and typesetting industry. Lorem Ipsum has been the industry's standard dummy text ever since the 1500s, when an unknown printer.</p>
      <p class="phone-line"><b>Ph:</b> 02 5550 1842</p>
    </article>
    <article class="list-item">
      <div class="contact-head"><h2 class="item-title">Kelvale</h2>
        <span class="contact-tools">
          <svg width="12" height="14" viewBox="0 0 12 14"><path d="M1 3h10M4 3V1h4v2M2 3l1 10h6l1-10" fill="none" stroke="#555" stroke-width="1.3"/></svg>
          <svg width="12" height="14" viewBox="0 0 12 14"><path d="M6 13C2 8 1 6 1 5a5 5 0 0110 0c0 1-1 3-5 8z" fill="none" stroke="#555" stroke-width="1.3"/><circle cx="6" cy="5" r="1.6" fill="#555"/></svg>
        </span></div>
      <p class="item-body">Lorem Ipsum is simply dummy text of the printing and typesetting industry. Lorem Ipsum has been the industry's standard dummy text ever since the 1500s, when an unknown printer.</p>
      <p class="phone-line"><b>Ph:</b> 02 5550 1842</p>
    </article>
    <article class="list-item">
      <div class="contact-head"><h2 class="item-title">Harbourside</h2>
        <span class="contact-tools">
          <svg width="12" height="14" viewBox="0 0 12 14"><path d="M1 3h10M4 3V1h4v2M2 3l1 10h6l1-10" fill="none" stroke="#555" stroke-width="1.3"/></svg>
          <svg width="12" height="14" viewBox="0 0 12 14"><path d="M6 13C2 8 1 6 1 5a5 5 0 0110 0c0 1-1 3-5 8z" fill="none" stroke="#555" stroke-width="1.3"/><circle cx="6" cy="5" r="1.6" fill="#555"/></svg>
        </span></div>
      <p class="item-body">Lorem Ipsum is simply dummy text of the printing and typesetting industry. Lorem Ipsum has been the industry's standard dummy text ever since the 1500s, when an unknown printer.</p>
      <p class="phone-line"><b>Ph:</b> 02 5550 1842</p>
    </article>
  </section>

  <!-- Articles list screen -->
  <section class="screen articles-screen">
    <div class="status-bar"><span>Carrier</span><span class="time">5:21 PM</span><span>100%</span></div>
    <header class="nav-bar">
      <svg class="menu-toggle" width="18" height="14" viewBox="0 0 18 14"><path d="M0 1h18M0 7h18M0 13h18" stroke="#fff" stroke-width="2"/></svg>
      Articles List
    </header>
    <article class="list-item article">
      <svg class="star" width="18" height="18" viewBox="0 0 24 24"><path d="M12 2l3 7 7 .6-5.3 4.7 1.6 7.2L12 17.8 5.7 21.5l1.6-7.2L2 9.6 9 9z" fill="var(--star)"/></svg>
      <div><h2 class="item-title">Work and Study Pathways</h2>
        <p class="item-body">Lorem Ipsum is simply dummy text of the printing and typesetting industry. Lorem Ipsum has been the industry's standard dummy text ever since the 1500s.</p>
        <span class="read-more">Read More&gt;&gt;</span></div>
    </article>
    <article class="list-item article">
      <svg class="star" width="18" height="18" viewBox="0 0 24 24"><path d="M12 2l3 7 7 .6-5.3 4.7 1.6 7.2L12 17.8 5.7 21.5l1.6-7.2L2 9.6 9 9z" fill="var(--star)"/></svg>
      <div><h2 class="item-title">Community Health Services</h2>
        <p class="item-body">Lorem Ipsum is simply dummy text of the printing and typesetting industry. Lorem Ipsum has been the industry's standard dummy text ever since the 1500s.</p>
        <span class="read-more">Read More&gt;&gt;</span></div>
    </article>
    <article class="list-item article">
      <svg class="star" width="18" height="18" viewBox="0 0 24 24"><path d="M12 2l3 7 7 .6-5.3 4.7 1.6 7.2L12 17.8 5.7 21.5l1.6-7.2L2 9.6 9 9z" fill="none" stroke="var(--star-outline)" stroke-width="1.5"/></svg>
      <div><h2 class="item-title">Business and Finance</h2>
        <p class="item-body">Lorem Ipsum is simply dummy text of the printing and typesetting industry. Lorem Ipsum has been the industry's standard dummy text ever since the 1500s.</p>
        <span class="read-more">Read More&gt;&gt;</span></div>
    </article>
  </section>

</main>
</body>
</html>
```